Red design in a sea of blue ocean

We need a new vehicle wrap that will stand out and will be noticed over all other contractors wraps . Bright coloring easy to ready name, number and services. Attached are some stand out designs to draw insight from.

++Our business card design is also uploaded. Fee free to take inspiration from the card design swapping colors.

Company: Dralto Power Max +
Services : residential Service, Commercial Service New Construction
Smart Homes, Solar, LED lighting,

Additional Partnered Services :
Hvac, Plumbing, Window Cleaning Christmas alighting, Home and Vacation Rental cleaning, car detailing

Please make designs on

Brenvik t 270 with a utility shell
Brenvik cargo high roof
Brenvik cargo link

Target Market(s)

Home owners

Industry/Entity Type

Electric Company

Requirements
Must have
• Name, logo, services and phone number

```html
<!DOCTYPE html>
<html lang="en">
<head>
<meta charset="utf-8">
<title>Dralto Power Group – Wrap Side Panels</title>
<link rel="stylesheet" href="https://fonts.googleapis.com/css2?family=Montserrat:wght@600;700&family=Oswald:wght@500;600&display=swap">
<style>
  :root {
    --wrap-blue: #2b6cb5;
    --wrap-black: #0d0d0d;
    --stripe-green: #7cc143;
    --lime-text: #b5d43c;
    --web-yellow: #d9d62e;
    --white: #ffffff;
    --page: #ffffff;
  }
  * { margin: 0; padding: 0; box-sizing: border-box; }
  html, body { width: 1200px; height: 1200px; overflow: hidden; background: var(--page); }
  .canvas { position: relative; width: 1200px; height: 1200px; }

  .wrap-panel {
    position: absolute;
    left: 50px;
    width: 1100px;
    height: 470px;
    background: var(--wrap-blue);
    border-radius: 28px 60px 18px 18px;
    overflow: hidden;
  }
  .wrap-panel--icons { top: 70px; }
  .wrap-panel--list { top: 660px; }

  .wrap-bands { position: absolute; inset: 0; width: 100%; height: 100%; }

  .service-icons {
    position: absolute; left: 90px; top: 58px;
    display: grid; grid-template-columns: repeat(3, 86px); row-gap: 18px;
  }
  .service-icon {
    display: flex; flex-direction: column; align-items: center; gap: 4px;
    font-family: "Oswald", sans-serif; font-weight: 500; font-size: 11px;
    color: var(--lime-text); letter-spacing: 0.3px; text-transform: uppercase;
  }
  .service-icon svg { width: 48px; height: 48px; }
  .service-icons .spacer { visibility: hidden; }

  .core-services {
    position: absolute; left: 128px; top: 78px; list-style: none;
    font-family: "Oswald", sans-serif; font-weight: 500; font-size: 23px;
    line-height: 27px; color: var(--lime-text); text-transform: uppercase;
  }
  .core-services li::before {
    content: ""; display: inline-block; width: 8px; height: 8px; border-radius: 50%;
    background: var(--stripe-green); margin-right: 8px; vertical-align: middle;
  }

  .partner-services {
    position: absolute; left: 44px; top: 300px;
    font-family: "Oswald", sans-serif; font-weight: 600; font-size: 13px;
    line-height: 21px; color: var(--white); text-transform: uppercase; letter-spacing: 0.2px;
  }
  .partner-services .sep { color: var(--stripe-green); padding: 0 3px; }

  .brand {
    position: absolute; left: 372px; top: 112px;
    display: flex; align-items: center; gap: 12px;
  }
  .brand-dot { width: 56px; height: 56px; border-radius: 50%; background: var(--stripe-green); flex: none; }
  .brand-name {
    font-family: "Montserrat", sans-serif; font-weight: 600; font-size: 30px;
    line-height: 1.05; color: var(--wrap-blue); white-space: nowrap;
  }

  .website {
    position: absolute; left: 486px; top: 310px;
    font-family: "Montserrat", sans-serif; font-weight: 700; font-size: 17px;
    color: var(--web-yellow); white-space: nowrap;
  }
  .phone {
    position: absolute; left: 882px; top: 318px;
    font-family: "Montserrat", sans-serif; font-weight: 700; font-size: 24px;
    letter-spacing: 1.5px; color: var(--white); white-space: nowrap;
  }
</style>
</head>
<body>
<main class="canvas">

  <section class="wrap-panel wrap-panel--icons" aria-label="Side wrap, icon version">
    <svg class="wrap-bands" viewBox="0 0 1100 470" preserveAspectRatio="none" aria-hidden="true">
      <polygon points="290,0 660,0 900,470 540,470" fill="var(--wrap-black)"/>
      <polygon points="270,0 290,0 540,470 520,470" fill="var(--stripe-green)"/>
      <polygon points="660,0 680,0 920,470 900,470" fill="var(--stripe-green)"/>
      <rect x="0" y="420" width="1100" height="50" fill="var(--wrap-black)"/>
    </svg>

    <div class="service-icons">
      <div class="service-icon">
        <svg viewBox="0 0 48 48" fill="none" stroke="#fff" stroke-width="2.2">
          <rect x="14" y="6" width="20" height="38"/>
          <path d="M18 12h4M26 12h4M18 19h4M26 19h4M18 26h4M26 26h4M18 33h4M26 33h4"/>
        </svg>
        <span>Commercial</span>
      </div>
      <div class="service-icon">
        <svg viewBox="0 0 48 48" fill="none" stroke="#fff" stroke-width="2.2">
          <path d="M6 24 24 8l18 16"/><path d="M11 20v22h26V20"/><rect x="20" y="30" width="8" height="12"/>
        </svg>
        <span>Residential</span>
      </div>
      <div class="service-icon spacer"><svg viewBox="0 0 48 48"></svg><span>–</span></div>
      <div class="service-icon">
        <svg viewBox="0 0 48 48" fill="none" stroke="#fff" stroke-width="2.2">
          <path d="M6 24 24 8l18 16"/><path d="M11 20v22h26V20"/>
          <path d="M17 28a10 10 0 0 1 14 0M20 32a5 5 0 0 1 8 0"/><circle cx="24" cy="36" r="1.4" fill="#fff"/>
        </svg>
        <span>Smart Homes</span>
      </div>
      <div class="service-icon">
        <svg viewBox="0 0 48 48" fill="none" stroke="#fff" stroke-width="2.2">
          <circle cx="24" cy="10" r="4"/><path d="M24 2v2M16 10h2M30 10h2M18 4l1.5 1.5M30 4l-1.5 1.5"/>
          <path d="M8 18h32l-4 18H12z"/><path d="M10 27h28M18 18l-2 18M30 18l2 18M24 18v18"/><path d="M24 36v8M18 44h12"/>
        </svg>
        <span>Solar</span>
      </div>
      <div class="service-icon">
        <svg viewBox="0 0 48 48" fill="none" stroke="#fff" stroke-width="2.2">
          <path d="M17 26a10 10 0 1 1 14 0c-2 2-3 4-3 7h-8c0-3-1-5-3-7z"/><path d="M20 37h8M21 41h6"/>
          <path d="M24 4v3M8 20h3M37 20h3M12 9l2 2M36 9l-2 2"/>
        </svg>
        <span>LED Lighting</span>
      </div>
    </div>

    <p class="partner-services">
      HVAC<span class="sep">|</span>Plumbing<span class="sep">|</span>Window Cleaning Christmas Alighting<br>
      Home and Vacation Rental Cleaning<span class="sep">|</span>Car Detailing
    </p>

    <div class="brand">
      <span class="brand-dot"></span>
      <span class="brand-name">Dralto<br>Power Group</span>
    </div>
    <p class="website">www.draltopowergroup.com</p>
    <p class="phone">555 01 01 01</p>
  </section>

  <section class="wrap-panel wrap-panel--list" aria-label="Side wrap, list version">
    <svg class="wrap-bands" viewBox="0 0 1100 470" preserveAspectRatio="none" aria-hidden="true">
      <polygon points="290,0 660,0 900,470 540,470" fill="var(--wrap-black)"/>
      <polygon points="270,0 290,0 540,470 520,470" fill="var(--stripe-green)"/>
      <polygon points="660,0 680,0 920,470 900,470" fill="var(--stripe-green)"/>
      <rect x="0" y="420" width="1100" height="50" fill="var(--wrap-black)"/>
    </svg>

    <ul class="core-services">
      <li>Residential</li>
      <li>Commercial</li>
      <li>Smart Homes</li>
      <li>Solar</li>
      <li>LED Lighting</li>
    </ul>

    <p class="partner-services">
      HVAC<span class="sep">|</span>Plumbing<span class="sep">|</span>Window Cleaning Christmas Alighting<br>
      Home and Vacation Rental Cleaning<span class="sep">|</span>Car Detailing
    </p>

    <div class="brand">
      <span class="brand-dot"></span>
      <span class="brand-name">Dralto<br>Power Group</span>
    </div>
    <p class="website">www.draltopowergroup.com</p>
    <p class="phone">555 01 01 01</p>
  </section>

</main>
</body>
</html>
```